Vintrel.com- International Goal Achievement Coach Needs Website Design

I need a web design for my new company called Vintrel. I help people who are stuck, people who have a big dream, but don't know how to get there. I help them to break their dreams down into small, manageable steps... and then I'm the "kick in the shin" to get them moving and thriving!

We can all be better- We can all DO better. I inspire people to Ride Onward in the direction of your dreams.

I have uploaded my logo along with some vintage champagne posters. Please use the vintage posters as inspiration. I like the bold, vintage look and feel. I would love the main colors of the design to be black, white and metallic gold. And to follow along this vintage look and feel. Please feel free to use the logo in black or metallic gold or white.

Target Market(s)

websites that I like- janetrulsby.com & hollyp.tv

I would like to also use the vintage champagne photos attached as inspiration as well.

Industry/Entity Type

It Company

Requirements
Must have
• Tabs should include: About, Work With Me, Praise, Giving Back

On the homepage add:
* Sign up for newsletter with space to enter name and email (No click throughs)
* Upcoming Events/Sessions
* Newsletter Posts
* Resources
* Praise Section

* Large photo on top with additional photos throughout the page/site.
Nice to have
• Any additions you can bring to the table would be greatly appreciated.

```html
<!DOCTYPE html>
<html lang="en">
<head>
<meta charset="utf-8">
<title>Vintrel — Goal Achievement Coaching</title>
<link rel="stylesheet" href="https://fonts.googleapis.com/css2?family=Cinzel:wght@400;700&family=Arimo:wght@400;700&display=swap">
<style>
  :root {
    --header-brown: #3d2d21;
    --header-brown-dark: #30231a;
    --gold: #d9bf7c;
    --gold-muted: #c9a866;
    --gold-light: #e6d08f;
    --gold-deep: #b8944f;
    --nav-text: #2a2018;
    --hero-text: #e9ddc8;
    --cta-orange: #e24a0c;
    --button-rust: #c6401b;
    --body-text: #3a3a3a;
    --heading-text: #1d1d1d;
    --white: #ffffff;
    --divider: #2e2620;
  }
  * { box-sizing: border-box; margin: 0; padding: 0; }
  html, body { width: 1200px; height: 1200px; overflow: hidden; background: var(--white); }
  body { font-family: "Arimo", Arial, sans-serif; position: relative; }

  .site-header {
    position: absolute; left: 0; top: 0; width: 1200px; height: 106px;
    background: linear-gradient(180deg, var(--header-brown) 0%, var(--header-brown-dark) 100%);
  }
  .brand { position: absolute; left: 100px; top: 20px; display: flex; align-items: center; height: 65px; }
  .brand-mark { width: 65px; height: 65px; border-radius: 50%; background: var(--gold); }
  .brand-divider { width: 1px; height: 64px; background: var(--gold-muted); margin: 0 12px 0 11px; }
  .brand-name { font-family: "Cinzel", serif; font-size: 30px; font-weight: 400; color: var(--gold); letter-spacing: 1px; }

  .testimonial { position: absolute; right: 100px; top: 22px; text-align: right; font-family: "Cinzel", serif; color: var(--gold-muted); }
  .testimonial-quote { font-size: 16px; line-height: 20px; letter-spacing: 0.3px; }
  .testimonial-author { font-size: 13px; font-weight: 700; font-style: italic; margin-top: 2px; }

  .main-nav {
    position: absolute; left: 0; top: 106px; width: 1200px; height: 50px;
    background: linear-gradient(180deg, var(--gold-light) 0%, var(--gold) 50%, var(--gold-deep) 100%);
    box-shadow: 0 2px 3px rgba(0,0,0,0.3);
  }
  .nav-list { position: absolute; left: 101px; top: 0; height: 50px; display: flex; align-items: center; list-style: none; }
  .nav-list li { font-size: 14px; font-weight: 700; color: var(--nav-text); letter-spacing: 0.4px; white-space: nowrap; }
  .nav-sep { margin: 0 14px; font-weight: 400; }
  .login-button {
    position: absolute; left: 982px; top: 13px; width: 80px; height: 25px;
    background: var(--button-rust); color: var(--white); font-size: 12px; font-weight: 700;
    display: flex; align-items: center; justify-content: center; border-radius: 2px;
  }
  .search-icon { position: absolute; left: 1081px; top: 122px; }

  .hero {
    position: absolute; left: 0; top: 156px; width: 1200px; height: 614px;
    background:
      linear-gradient(90deg, rgba(13,20,16,0) 35%, rgba(10,14,14,0.85) 70%, rgba(8,10,12,0.92) 100%),
      linear-gradient(180deg, #4a5a34 0%, #3c4a2a 45%, #6b5a3e 75%, #8a7150 100%);
  }
  .hero-rule { position: absolute; left: 0; top: 770px; width: 1200px; height: 5px; background: var(--divider); }
  .hero-copy { position: absolute; left: 565px; top: 254px; color: var(--hero-text); font-family: "Cinzel", serif; }
  .hero-title { font-size: 37px; font-weight: 700; letter-spacing: 0.6px; line-height: 44px; white-space: nowrap; }
  .hero-subtitle { font-size: 22px; font-weight: 400; margin-top: 6px; letter-spacing: 0.4px; white-space: nowrap; }
  .hero-free { font-size: 22px; font-weight: 700; margin-top: 10px; letter-spacing: 0.5px; }

  .signup-field {
    position: absolute; top: 393px; width: 245px; height: 50px; background: var(--white);
    padding-left: 19px; display: flex; align-items: center;
    font-size: 17px; color: #6f6a58; letter-spacing: 0.5px; word-spacing: 3px;
  }
  .signup-name { left: 565px; }
  .signup-email { left: 824px; }
  .signup-submit {
    position: absolute; left: 565px; top: 463px; width: 505px; height: 50px;
    background: var(--cta-orange); color: var(--white); font-size: 20px; font-weight: 700;
    display: flex; align-items: center; justify-content: center; letter-spacing: 0.5px; border-radius: 2px;
  }

  .feature-article { position: absolute; left: 100px; top: 822px; width: 750px; }
  .article-title { font-family: "Cinzel", serif; font-size: 21px; font-weight: 400; color: var(--heading-text); letter-spacing: 0.5px; line-height: 24px; white-space: nowrap; }
  .article-subtitle { font-family: "Cinzel", serif; font-size: 20px; font-weight: 400; color: var(--heading-text); letter-spacing: 0.8px; line-height: 28px; white-space: nowrap; }
  .article-photo { position: absolute; left: 2px; top: 70px; width: 200px; height: 200px; background: linear-gradient(135deg, #8d8a84, #5a5b62 50%, #8a6a4c); }
  .article-body {
    position: absolute; left: 222px; top: 66px; width: 526px;
    font-size: 16px; line-height: 21.7px; color: var(--body-text); text-align: justify; letter-spacing: 0.3px;
  }
  .read-more {
    position: absolute; left: 628px; top: 245px; width: 120px; height: 25px;
    background: var(--button-rust); color: var(--white); font-size: 13px; font-weight: 700;
    display: flex; align-items: center; justify-content: center; border-radius: 2px;
  }

  .sidebar-story { position: absolute; left: 880px; top: 826px; width: 190px; }
  .sidebar-photo { width: 189px; height: 128px; margin-left: 1px; background: linear-gradient(160deg, #8a8e8a, #6c706d 60%, #7d7a72); }
  .sidebar-text { margin-top: 16px; font-size: 12.5px; line-height: 16.8px; color: var(--body-text); text-align: justify; letter-spacing: 0.3px; }
</style>
</head>
<body>
  <header class="site-header">
    <div class="brand">
      <div class="brand-mark"></div>
      <div class="brand-divider"></div>
      <span class="brand-name">Vintrel</span>
    </div>
    <blockquote class="testimonial">
      <p class="testimonial-quote">“Vintrel kicked me out of my rut,<br>and now I’m living my dream life!”</p>
      <p class="testimonial-author">- Client Name</p>
    </blockquote>
  </header>

  <nav class="main-nav">
    <ul class="nav-list">
      <li>HOME</li><li class="nav-sep">/</li>
      <li>ABOUT</li><li class="nav-sep">/</li>
      <li>WORK&nbsp; WITH&nbsp; ME</li><li class="nav-sep">/</li>
      <li>PRAISE</li><li class="nav-sep">/</li>
      <li>GIVING&nbsp; BACK</li><li class="nav-sep">/</li>
      <li>PUBLICATIONS</li><li class="nav-sep">/</li>
      <li>SHOP</li><li class="nav-sep">/</li>
      <li>CONTACT</li>
    </ul>
    <div class="login-button">LOGIN</div>
  </nav>
  <svg class="search-icon" width="20" height="20" viewBox="0 0 20 20" aria-label="Search">
    <circle cx="7.5" cy="7.5" r="5.5" fill="none" stroke="#2a2018" stroke-width="2.4"/>
    <line x1="11.5" y1="11.5" x2="18" y2="18" stroke="#2a2018" stroke-width="3" stroke-linecap="round"/>
  </svg>

  <section class="hero" role="img" aria-label="Photograph of a small wooden shed on stilts among trees on a forested hillside"></section>
  <div class="hero-copy">
    <h1 class="hero-title">WE CAN ALL DO BETTER.</h1>
    <p class="hero-subtitle">SIGN UP FOR OUR 30-DAY PROGRAM TODAY.</p>
    <p class="hero-free">IT’S FREE.</p>
  </div>
  <div class="signup-field signup-name">FIRST NAME</div>
  <div class="signup-field signup-email">EMAIL ADDRESS</div>
  <div class="signup-submit">GET STARTED</div>
  <div class="hero-rule"></div>

  <article class="feature-article">
    <h2 class="article-title">LETTING GO OF THE PAST TO MOVE FORWARD</h2>
    <h3 class="article-subtitle">ONE WOMAN’S JOURNEY TO FINANCIAL SUCCESS</h3>
    <div class="article-photo" role="img" aria-label="Photograph of a woman giving to a seated man on a city street"></div>
    <p class="article-body">Vivamus aliquam, risus vulputate laoreet fermentum, sem ipsum placerat felis, ac egestas orci tellus in ante. Etiam non viverra erat, ultrices sollicitudin lacus. Nunc faucibus sollicitudin turpis, at sollicitudin odio mattis eu. In ligula justo, viverra vitae velit hendrerit, ullamcorper commodo velit. Cras egestas nec eros a vulputate. Quisque eleifend sapien sed sem bibendum feugiat. Suspendisse nulla eros, sollicitudin egestas iaculis et, blandit.</p>
    <div class="read-more">READ MORE</div>
  </article>

  <aside class="sidebar-story">
    <div class="sidebar-photo" role="img" aria-label="Photograph of a man in a suit walking across a road seen from above"></div>
    <p class="sidebar-text">Vivamus aliquam, risus vulputate laoreet fermentum, sem ipsum placerat felis, ac egestas orci tellus in ante. Etiam non viverra erat, ultrices sollicitudin lacus. Nunc faucibus sollicitudin turpis, at.</p>
  </aside>
</body>
</html>
```